Need a business card created for my Heating and Air-conditioning business

We are a new Air Conditioning , Refrigeration and Heating business called Frost & Cinder HVAC/R - we do repairs, maintenance and installations.

Our motto is "Skilled Precision - Superior Value"

Information needed on the card:
Neil Fardon
778-555-4817
www.frosthvac-example.ca
info@frosthvac-example.ca

```html
<!DOCTYPE html>
<html lang="en">
<head>
<meta charset="utf-8">
<title>Frost &amp; Cinder HVAC/R — Business Card</title>
<link rel="stylesheet" href="https://fonts.googleapis.com/css2?family=Montserrat:wght@400;500;700&family=Oswald:wght@400;500&display=swap">
<style>
  :root {
    --stage: #9b9b9b;
    --card-dark: #1b1b1b;
    --card-light: #e3eaf5;
    --white: #ffffff;
    --ink: #1d1d1d;
    --navy: #17497a;
    --muted: #8e8e8e;
    --ice: #5ea3e3;
    --ember: #d8192d;
    --gas: #e0931c;
    --volt: #23b34a;
    --air: #cfcfcf;
    --indoor: #e2c21a;
  }
  * { box-sizing: border-box; margin: 0; padding: 0; }
  html, body { width: 1200px; height: 1000px; overflow: hidden; }
  body { background: var(--stage); position: relative; font-family: "Montserrat", sans-serif; }

  .card {
    position: absolute;
    left: 296px;
    width: 607px;
    height: 350px;
    border-radius: 24px;
    overflow: hidden;
  }
  .card--front { top: 129px; background: var(--card-dark); }
  .card--back  { top: 531px; background: var(--card-light); }

  /* Front: brand name block */
  .brand {
    position: absolute;
    display: flex;
    align-items: center;
    gap: 16px;
  }
  .brand__mark {
    border-radius: 50%;
    flex: none;
  }
  .brand__name {
    font-family: "Montserrat", sans-serif;
    font-weight: 500;
    line-height: 1.15;
  }
  .card--front .brand { left: 132px; top: 66px; }
  .card--front .brand__mark { width: 120px; height: 120px; border: 2px solid var(--white); }
  .card--front .brand__name { color: var(--white); font-size: 34px; }

  /* Front: services row */
  .services {
    position: absolute;
    left: 0; right: 0; top: 271px;
    list-style: none;
  }
  .service {
    position: absolute;
    top: 0;
    width: 90px;
    margin-left: -45px;
    text-align: center;
  }
  .service svg { width: 30px; height: 30px; display: block; margin: 0 auto; }
  .service__label {
    display: block;
    margin-top: 12px;
    font-family: "Oswald", sans-serif;
    font-size: 7.5px;
    letter-spacing: 1.4px;
    color: var(--white);
    white-space: nowrap;
  }

  /* Back */
  .card--back .brand { left: 34px; top: 42px; gap: 12px; }
  .card--back .brand__mark { width: 96px; height: 96px; border: 2px solid var(--ink); }
  .card--back .brand__name { color: var(--ink); font-size: 22px; }

  .backdrop-art {
    position: absolute;
    left: 253px; top: 0;
    width: 354px; height: 350px;
    background: radial-gradient(ellipse at 70% 75%, rgba(255,255,255,0.95) 0%, rgba(255,255,255,0.7) 40%, rgba(255,255,255,0) 75%);
  }

  .person { position: absolute; left: 32px; top: 162px; }
  .person__name {
    font-family: "Oswald", sans-serif;
    font-weight: 400;
    font-size: 34px;
    color: var(--navy);
    line-height: 1;
    transform: scaleX(0.86);
    transform-origin: left;
  }
  .person__role {
    margin-top: 8px;
    font-family: "Montserrat", sans-serif;
    font-weight: 700;
    font-size: 10px;
    letter-spacing: 2.6px;
    color: var(--muted);
  }

  .contact { position: absolute; left: 32px; top: 259px; list-style: none; }
  .contact__item {
    display: flex;
    align-items: center;
    height: 21px;
    font-size: 17px;
    font-weight: 400;
    color: var(--ink);
  }
  .contact__item svg { width: 13px; height: 13px; margin-right: 13px; flex: none; }
</style>
</head>
<body>

<section class="card card--front" aria-label="Card front">
  <div class="brand">
    <span class="brand__mark" aria-hidden="true"></span>
    <p class="brand__name">Frost &amp; Cinder<br>HVAC/R</p>
  </div>

  <ul class="services">
    <li class="service" style="left:159px">
      <svg viewBox="0 0 30 30" fill="none" stroke="var(--ice)" stroke-width="1.2" stroke-linecap="round">
        <path d="M15 2v26M3.7 8.5l22.6 13M3.7 21.5l22.6-13"/>
        <path d="M12 4.5l3 3 3-3M12 25.5l3-3 3 3"/>
      </svg>
      <span class="service__label">REFRIGERATION</span>
    </li>
    <li class="service" style="left:231px">
      <svg viewBox="0 0 30 30" fill="none" stroke="var(--ember)" stroke-width="1.3">
        <circle cx="15" cy="15" r="13.5"/>
        <circle cx="15" cy="15" r="10"/>
        <circle cx="15" cy="15" r="1.8"/>
        <path d="M15 13c-1-4 1-6 3-5s1 4-3 5zM17 15.5c4-.5 5.5 1.5 4.5 3.5s-4 1-4.5-3.5zM13.5 16.5c-2 3.5-4.5 3.5-5.5 1.5s1.5-3.5 5.5-1.5zM13 14c-3.5-1.5-3.5-4-1.5-4.8s3 1.8 1.5 4.8z"/>
      </svg>
      <span class="service__label">HEAT PUMPS</span>
    </li>
    <li class="service" style="left:284px">
      <svg viewBox="0 0 30 30">
        <path fill="var(--gas)" d="M15 1c2 5 8 9 8 17a8 8 0 0 1-16 0c0-4 2-6 3-8 0 3 1 5 3 5-1-5 0-10 2-14z"/>
        <path fill="var(--card-dark)" d="M15 17c1 2 3 3 3 6a3 3 0 0 1-6 0c0-2 2-3 3-6z"/>
      </svg>
      <span class="service__label">GAS</span>
    </li>
    <li class="service" style="left:335px">
      <svg viewBox="0 0 30 30" fill="none" stroke="var(--volt)" stroke-width="1.4" stroke-linejoin="round">
        <circle cx="15" cy="15" r="13.5"/>
        <path d="M16.5 6l-6 10h4.5l-1.5 8 6-10H15z"/>
      </svg>
      <span class="service__label">ELECTRICAL</span>
    </li>
    <li class="service" style="left:398px">
      <svg viewBox="0 0 30 30" fill="none" stroke="var(--air)" stroke-width="1.4" stroke-linecap="round">
        <path d="M2 11h20a3.5 3.5 0 1 0-3.5-3.5"/>
        <path d="M2 16h24a3 3 0 1 1-3 3"/>
        <path d="M4 21h12a3 3 0 1 1-3 3"/>
      </svg>
      <span class="service__label">VENTILATION</span>
    </li>
    <li class="service" style="left:459px">
      <svg viewBox="0 0 30 30" fill="none" stroke="var(--indoor)" stroke-width="1.2">
        <circle cx="15" cy="15" r="13.5"/>
        <circle cx="15" cy="15" r="6.5"/>
        <path d="M15 8.5V5M15 21.5V25M8.5 15H5M21.5 15H25M10.4 10.4l-2.5-2.5M19.6 19.6l2.5 2.5M19.6 10.4l2.5-2.5M10.4 19.6l-2.5 2.5"/>
        <circle cx="13" cy="13.5" r="1"/><circle cx="17" cy="14" r="1"/><circle cx="15" cy="17" r="1"/>
      </svg>
      <span class="service__label">INDOOR AIR</span>
    </li>
  </ul>
</section>

<section class="card card--back" aria-label="Card back">
  <div class="backdrop-art" role="img" aria-label="Large faint white polar bear silhouette breathing swirling wind, decorative background"></div>

  <div class="brand">
    <span class="brand__mark" aria-hidden="true"></span>
    <p class="brand__name">Frost &amp; Cinder<br>HVAC/R</p>
  </div>

  <div class="person">
    <h1 class="person__name">Neil Fardon</h1>
    <p class="person__role">OWNER</p>
  </div>

  <ul class="contact">
    <li class="contact__item">
      <svg viewBox="0 0 24 24" fill="var(--navy)"><path d="M6.6 2.5l3 .4 1.2 5-2.4 1.7a13 13 0 0 0 6 6l1.7-2.4 5 1.2.4 3c-.2 1.8-1.6 3-3.5 3C9.5 20.4 3.6 14.5 3.6 6c0-1.9 1.2-3.3 3-3.5z"/></svg>
      778-555-4817
    </li>
    <li class="contact__item">
      <svg viewBox="0 0 24 24" fill="none" stroke="var(--navy)" stroke-width="2"><circle cx="12" cy="12" r="10"/><path d="M2 12h20M12 2c3 3 4 6.5 4 10s-1 7-4 10c-3-3-4-6.5-4-10s1-7 4-10zM4 7h16M4 17h16"/></svg>
      www.frosthvac-example.ca
    </li>
    <li class="contact__item">
      <svg viewBox="0 0 24 24" fill="none" stroke="var(--navy)" stroke-width="2"><rect x="1.5" y="5" width="21" height="14" fill="var(--navy)"/><path d="M1.5 5l10.5 8 10.5-8M1.5 19l8-7M22.5 19l-8-7" stroke="var(--card-light)" stroke-width="1.5"/></svg>
      info@frosthvac-example.ca
    </li>
  </ul>
</section>

</body>
</html>
```